Brightwell Homes Guide Business card

I have had at the logo designed here and attached. The business compares off the plan apartments in Sydney and provides quick comparison for new home buyers e.g price, floor plans and location. I would like the complimentary colours used on the business card. I would like it be unique but also look professional. I also have a website to gain inspiration from www.brightwellhomesguide.com.au
Updates
Industry/Entity Type
Business
Contact Information for Business Card
Helen Vostrakis
Director of Business Development
e: helen.vostrakis@brightwellhomesguide.com.au
p: (02) 8143 7692
m: 0431 572 908
w: www.brightwellhomesguide.com.au
Look and feel
Each slider illustrates characteristics of the customer's brand and the style your logo design should communicate.

```html
<!DOCTYPE html>
<html lang="en">
<head>
<meta charset="utf-8">
<title>Brightwell Homes Guide – Business Card</title>
<link href="https://fonts.googleapis.com/css2?family=Arimo:wght@400;700&display=swap" rel="stylesheet">
<style>
  :root{
    --bg:#2b2b2b;
    --card:#fbfbfb;
    --green:#7cb82f;
    --brand-green:#7dc242;
    --blue:#1e8fd6;
    --accent:#f26522;
    --ink:#2f3327;
    --ink-soft:#4d5e36;
    --on-green:#e6f2d6;
    --title:#c4e0a0;
  }
  *{margin:0;padding:0;box-sizing:border-box}
  html,body{width:1200px;height:873px;overflow:hidden;background:var(--bg)}
  body{position:relative;font-family:"Arimo",Arial,sans-serif}
  .card{
    position:absolute;width:520px;height:310px;background:var(--card);
    overflow:hidden;box-shadow:0 10px 30px rgba(0,0,0,.45);
  }
  .card--front{left:60px;top:140px}
  .card--back{left:620px;top:420px}
  .card__swoosh{position:absolute;inset:0;width:100%;height:100%}
  .brand{position:absolute;display:flex;align-items:center;gap:10px;white-space:nowrap}
  .brand__mark{background:var(--accent);flex:none}
  .brand__name{color:var(--brand-green);font-weight:400;letter-spacing:-.5px}
  .card--front .brand{left:56px;top:92px}
  .card--front .brand__mark{width:16px;height:16px}
  .card--front .brand__name{font-size:32px}
  .card--back .brand{left:0;right:0;top:40px;justify-content:center}
  .card--back .brand__mark{width:11px;height:11px}
  .card--back .brand__name{font-size:23px}
  .person{position:absolute;right:302px;top:178px;text-align:right;white-space:nowrap}
  .person__name{font-size:15px;font-weight:700;color:var(--ink)}
  .person__title{font-size:10.5px;color:var(--title);margin-top:3px}
  .person__address{font-size:12.5px;color:var(--ink-soft);margin-top:20px;line-height:1.45}
  .divider{position:absolute;left:232px;top:168px;width:1.5px;height:120px;background:var(--on-green);opacity:.85}
  .contact{position:absolute;left:248px;top:160px;list-style:none}
  .contact li{display:flex;align-items:center;gap:9px;font-size:11px;color:var(--on-green);height:21px;white-space:nowrap}
  .contact svg{width:14px;height:12px;flex:none}
  .contact .contact__web{font-weight:700;color:var(--ink);font-size:12px;margin-top:6px}
</style>
</head>
<body>

<section class="card card--front" aria-label="Business card front">
  <svg class="card__swoosh" viewBox="0 0 520 310" preserveAspectRatio="none" aria-hidden="true">
    <path d="M110 310 C 250 260 400 190 520 118 L520 310 Z" fill="var(--green)"/>
    <path d="M110 310 C 250 260 400 190 520 118" fill="none" stroke="var(--blue)" stroke-width="6"/>
  </svg>
  <div class="brand">
    <span class="brand__mark"></span>
    <span class="brand__name">Brightwell Homes Guide</span>
  </div>
</section>

<section class="card card--back" aria-label="Business card back">
  <svg class="card__swoosh" viewBox="0 0 520 310" preserveAspectRatio="none" aria-hidden="true">
    <path d="M0 195 C 150 128 330 100 520 112 L520 310 L0 310 Z" fill="var(--green)"/>
    <path d="M0 195 C 150 128 330 100 520 112" fill="none" stroke="var(--blue)" stroke-width="5"/>
  </svg>
  <div class="brand">
    <span class="brand__mark"></span>
    <span class="brand__name">Brightwell Homes Guide</span>
  </div>

  <div class="person">
    <p class="person__name">Helen Vostrakis</p>
    <p class="person__title">Director of Business Development</p>
    <p class="person__address">58 Marlow Street,<br>Castlebrook, NSW 2765</p>
  </div>

  <div class="divider"></div>

  <ul class="contact">
    <li>
      <svg viewBox="0 0 14 12" aria-hidden="true"><path d="M1 4 C1 1 13 1 13 4 L10 5 L10 3.5 C8 3 6 3 4 3.5 L4 5 Z M3 6 H11 L12 11 H2 Z" fill="var(--ink)"/></svg>
      (02) 8143 7692
    </li>
    <li>
      <svg viewBox="0 0 14 12" aria-hidden="true"><rect x="4" y="0" width="6" height="12" rx="1" fill="var(--ink)"/><rect x="5" y="1.5" width="4" height="7" fill="var(--on-green)"/></svg>
      0431 572 908
    </li>
    <li>
      <svg viewBox="0 0 14 12" aria-hidden="true"><rect x="0.5" y="1.5" width="13" height="9" fill="var(--ink)"/><path d="M0.5 1.5 L7 7 L13.5 1.5" fill="none" stroke="var(--on-green)" stroke-width="1"/></svg>
      helen.vostrakis@brightwellhomesguide.com.au
    </li>
    <li class="contact__web">www.brightwellhomesguide.com.au</li>
  </ul>
</section>

</body>
</html>
```